" Temos como propósito desenvolver pessoas e proporcionar saúde transformando vidas e sorrisos. Acreditamos que a educação muda pessoas e essas transformam o mundo. E que a manutenção da saúde bucal é fundamental para a saúde geral e o aumento da auto-estima do indivíduo. Nosso principal serviço são os cursos de ortodontia para dentistas já formados (pós-graduação e cursos livres de ortodontia). Temos alguns outros cursos também para dentistas em outras áreas. "

```html
<!DOCTYPE html>
<html lang="pt-BR">
<head>
<meta charset="utf-8">
<title>Ortelle — Envelope Saco</title>
<link rel="stylesheet" href="https://fonts.googleapis.com/css2?family=Montserrat:wght@400;600;700&display=swap">
<style>
  :root {
    --navy: #2b4456;
    --maroon: #7a1f45;
    --white: #ffffff;
    --stage: #e4e4e4;
  }
  * { margin: 0; padding: 0; box-sizing: border-box; }
  html, body { width: 1200px; height: 1200px; overflow: hidden; }
  body {
    background: var(--stage);
    font-family: "Montserrat", sans-serif;
    position: relative;
  }
  .envelope {
    position: absolute;
    top: 260px;
    width: 520px;
    height: 680px;
    background: var(--white);
    box-shadow: 0 14px 26px rgba(0,0,0,.22);
  }
  .envelope--back { left: 50px; }
  .envelope--front { left: 630px; }
  .envelope svg { position: absolute; inset: 0; display: block; }

  .wordmark {
    position: absolute;
    font-family: "Montserrat", sans-serif;
    font-weight: 700;
    letter-spacing: .01em;
    white-space: nowrap;
  }
  .envelope--back .wordmark {
    left: 26px; top: 606px;
    font-size: 34px;
    color: var(--white);
  }
  .envelope--front .wordmark {
    left: 36px; top: 288px;
    font-size: 62px;
    color: var(--navy);
  }

  .contact {
    position: absolute;
    left: 318px;
    top: 548px;
    list-style: none;
    color: var(--white);
    font-size: 9.5px;
    line-height: 1.25;
  }
  .contact li {
    display: flex;
    align-items: center;
    gap: 8px;
    margin-bottom: 10px;
  }
  .contact .icon {
    flex: none;
    width: 16px; height: 16px;
    border-radius: 50%;
    background: var(--white);
    display: flex; align-items: center; justify-content: center;
  }
  .contact .icon svg { position: static; width: 10px; height: 10px; }
</style>
</head>
<body>

  <!-- Envelope back with flap -->
  <section class="envelope envelope--back" aria-label="Verso do envelope">
    <svg viewBox="0 0 520 680" width="520" height="680">
      <rect width="520" height="680" fill="var(--navy)"/>
      <path d="M0,0 H520 V290 C480,470 280,585 120,552 C60,540 22,505 0,468 Z" fill="var(--maroon)"/>
      <path d="M0,0 H520 V250 C470,420 260,560 120,520 C60,505 20,470 0,432 Z" fill="var(--white)"/>
      <path d="M520,270 C476,446 270,574 120,538 C60,524 21,489 0,452" fill="none" stroke="var(--white)" stroke-width="2"/>
      <path class="flap" d="M36,0 H484 L520,0 V8 L494,72 H26 L0,8 V0 Z" fill="var(--navy)"/>
    </svg>
    <span class="wordmark">Ortelle</span>
  </section>

  <!-- Envelope front -->
  <section class="envelope envelope--front" aria-label="Frente do envelope">
    <svg viewBox="0 0 520 680" width="520" height="680">
      <rect width="520" height="680" fill="var(--navy)"/>
      <path d="M0,0 H222 C372,150 366,530 150,680 H0 Z" fill="var(--maroon)"/>
      <path d="M0,0 H190 C330,140 330,520 120,680 H0 Z" fill="var(--white)"/>
      <path d="M206,0 C351,145 348,525 135,680" fill="none" stroke="var(--white)" stroke-width="2"/>
    </svg>
    <span class="wordmark">Ortelle</span>

    <ul class="contact">
      <li>
        <span class="icon"><svg viewBox="0 0 10 10"><path d="M2.2,1 L3.8,1 L4.4,3 L3.3,3.8 C3.8,5 4.9,6.2 6.2,6.7 L7,5.6 L9,6.2 V7.8 C9,8.5 8.4,9 7.7,9 C4,8.7 1.3,6 1,2.3 C1,1.6 1.5,1 2.2,1 Z" fill="var(--navy)"/></svg></span>
        <span>11 4002-7318<br>11 4002-7319</span>
      </li>
      <li>
        <span class="icon"><svg viewBox="0 0 10 10"><rect x="1" y="2.5" width="8" height="5.5" rx=".6" fill="var(--navy)"/><path d="M1.3,2.9 L5,5.6 L8.7,2.9" fill="none" stroke="var(--white)" stroke-width=".8"/></svg></span>
        <span>contato@ortelle.com.br</span>
      </li>
      <li>
        <span class="icon"><svg viewBox="0 0 10 10"><circle cx="5" cy="5" r="3.8" fill="none" stroke="var(--navy)" stroke-width=".9"/><ellipse cx="5" cy="5" rx="1.6" ry="3.8" fill="none" stroke="var(--navy)" stroke-width=".8"/><path d="M1.2,5 H8.8" stroke="var(--navy)" stroke-width=".8"/></svg></span>
        <span>www.ortelle.com.br</span>
      </li>
      <li>
        <span class="icon"><svg viewBox="0 0 10 10"><path d="M5,9.3 C3,6.6 2,5 2,3.8 A3,3 0 0 1 8,3.8 C8,5 7,6.6 5,9.3 Z" fill="var(--navy)"/><circle cx="5" cy="3.8" r="1.1" fill="var(--white)"/></svg></span>
        <span>Rua das Acácias, 120<br>Jardim Sul - Campinas - SP - 13000-000</span>
      </li>
    </ul>
  </section>

</body>
</html>
```